Dorin Commercial Truck / Trailer / RV Repair

Need a billboard design for our shop. Will include our logo below and want the word DORIN on the top without the circle. Straighten out the letter "M" on the logo as well. Also will include a rough draft of a design and words I had in mind. All the words need to be included but the layout and design is up to you. Open to all options just needs to be easy to see and understand the message from the highway.

```html
<!DOCTYPE html>
<html lang="en">
<head>
<meta charset="utf-8">
<title>Dorin Commercial Truck / Trailer / RV Repair — Billboard</title>
<link rel="stylesheet" href="https://fonts.googleapis.com/css2?family=Barlow:wght@400;600;700&family=Manrope:wght@500;600&display=swap">
<style>
  :root {
    --page: #e9edf1;
    --panel-sky: #8fdcef;
    --band-royal: #1f38e0;
    --brand-navy: #2a5279;
    --accent-orange: #f0531f;
    --caption-slate: #2d4a66;
    --call-yellow: #f4f316;
    --ink-dark: #1a1f26;
  }
  * { margin: 0; padding: 0; box-sizing: border-box; }
  html, body { width: 1200px; height: 900px; overflow: hidden; }
  body {
    background: var(--page);
    font-family: "Barlow", Arial, sans-serif;
    position: relative;
  }
  .billboard {
    position: absolute;
    left: 30px; top: 235px;
    width: 1140px; height: 430px;
    background: var(--panel-sky);
    overflow: hidden;
  }
  .brand {
    position: absolute;
    left: 70px; top: 20px;
  }
  .brand-name {
    font-family: "Barlow", Arial, sans-serif;
    font-weight: 700;
    font-size: 150px;
    line-height: 1;
    letter-spacing: 6px;
    color: var(--brand-navy);
  }
  .service-tag {
    position: absolute;
    font-size: 19px;
    color: var(--accent-orange);
  }
  .tag-commercial { left: 70px;  top: 202px; }
  .tag-repair     { left: 300px; top: 228px; }
  .tag-shop       { left: 515px; top: 254px; }

  .service-list {
    position: absolute;
    left: 690px; top: 32px;
    width: 430px;
  }
  .service-row {
    display: grid;
    grid-template-columns: 92px 1fr;
    margin-bottom: 28px;
  }
  .service-row:nth-child(2) { padding-left: 40px; }
  .service-row:nth-child(3) { padding-left: 120px; }
  .service-label { font-size: 22px; color: var(--accent-orange); }
  .service-note  { font-size: 21px; line-height: 1.3; color: var(--caption-slate); }

  .call-band {
    position: absolute;
    left: 0; bottom: 0;
    width: 100%; height: 140px;
    background: var(--band-royal);
    font-family: "Manrope", Verdana, sans-serif;
    color: var(--call-yellow);
  }
  .call-line {
    position: absolute;
    left: 30px; top: 18px;
    font-size: 66px;
    font-weight: 500;
    white-space: nowrap;
  }
  .call-word { margin-right: 26px; }
  .quote-line {
    position: absolute;
    right: 28px; top: 36px;
    font-size: 30px;
    font-weight: 600;
  }
  .storage-note {
    position: absolute;
    right: 88px; top: 88px;
    font-size: 15px;
    font-weight: 500;
    letter-spacing: 0.5px;
  }
</style>
</head>
<body>
  <section class="billboard">
    <div class="brand">
      <div class="brand-name">DORIN</div>
    </div>
    <span class="service-tag tag-commercial">Commercial</span>
    <span class="service-tag tag-repair">Repair</span>
    <span class="service-tag tag-shop">Shop</span>

    <div class="service-list">
      <div class="service-row">
        <span class="service-label">Truck</span>
        <span class="service-note">pic of semi Truck</span>
      </div>
      <div class="service-row">
        <span class="service-label">Trailer</span>
        <span class="service-note">pic of semi Trailer<br>can be a variety</span>
      </div>
      <div class="service-row">
        <span class="service-label">RV</span>
        <span class="service-note">pic of RV<br>can be a variety</span>
      </div>
    </div>

    <div class="call-band">
      <div class="call-line"><span class="call-word">Call</span>888. 555 0142</div>
      <div class="quote-line">Or Come by a Quote !</div>
      <div class="storage-note">Parking and Storage Available</div>
    </div>
  </section>
</body>
</html>
```